COMING SOON PAGE for BEAUTY WEBSITE

Looking for a very beautiful, high end coming soon page for the site, www.glowparlorqz.com

looking for the site to have a bit of text and fade thru a few images -- beautiful fonts, modern airy feel.

Text on page:

it doesn't have to be complicated
glowparlorqz.com coming soon
beauty, simplified.

Please use all lowercase and place the logo somewhere on the page...logo attached and images attached -- happy to provide more images if necessary

You can play with images, zoom in, dont need to use whole image, etc....modern, classy, airy.

thanks.

Target Market(s)

35-60 year old women, modern, elegant, look conscious

Number of Pages Required

1 page

Font styles to use
Sans Serif

Requirements
Must have
• Images fade from one to other slowly and elegantly -- or slide, etc..some sort of elegant transition
• Opaque, airy feel
• logo must be present and easy to identify
Should not have
• NO SOUND
• NO SCRIPT TEXT

```html
<!DOCTYPE html>
<html lang="en">
<head>
<meta charset="utf-8">
<title>glowparlorqz — coming soon</title>
<link href="https://fonts.googleapis.com/css2?family=Quicksand:wght@300;400;500&display=swap" rel="stylesheet">
<style>
  :root {
    --stage-top: #414141;
    --stage-bottom: #202020;
    --teal: #5ccfcf;
    --teal-strong: #4fd3d3;
    --white: #ffffff;
    --bar-dark: #0c0c0c;
    --bar-mid: #222222;
    --wall-light: #a9a9a7;
    --wall-mid: #7c7b77;
    --wall-dark: #3b3b38;
    --field: #f1f5f4;
    --placeholder: #8f9695;
    --icon-ink: #1a1a1a;
    --photo-top: #5a4a40;
    --photo-mid: #e6e4ea;
    --photo-low: #cfcdd3;
    --photo-bottom: #141414;
  }
  * { margin: 0; padding: 0; box-sizing: border-box; }
  html, body { width: 1200px; height: 960px; overflow: hidden; }
  body {
    background: linear-gradient(180deg, var(--stage-top) 0%, #333 55%, var(--stage-bottom) 100%);
    font-family: "Quicksand", sans-serif;
    position: relative;
  }
  .site {
    position: absolute; left: 28px; top: 175px; width: 1144px; height: 643px;
    overflow: hidden;
    background:
      radial-gradient(ellipse 520px 420px at 260px 180px, var(--wall-light) 0%, transparent 100%),
      radial-gradient(ellipse 500px 380px at 900px 240px, #85847f 0%, transparent 100%),
      linear-gradient(180deg, var(--wall-mid) 0%, #5e5d59 60%, var(--wall-dark) 100%);
  }
  .hero-photo {
    position: absolute; left: 206px; top: 81px; width: 270px; height: 562px;
    border-radius: 10px 10px 0 0;
    background: linear-gradient(180deg,
      var(--photo-top) 0%, var(--photo-top) 24%,
      var(--photo-mid) 30%, var(--photo-low) 68%,
      var(--photo-bottom) 76%, var(--photo-bottom) 100%);
    opacity: 0.9;
  }
  .topbar { position: absolute; left: 0; top: 0; width: 1144px; height: 40px; }
  .social { position: absolute; top: 10px; left: 950px; display: flex; gap: 9px; }
  .social span {
    width: 17px; height: 17px; background: var(--white); border-radius: 2px;
    display: flex; align-items: center; justify-content: center;
  }
  .social span::after {
    content: ""; width: 7px; height: 7px; border: 1.5px solid var(--icon-ink); border-radius: 50%;
  }
  .menu { position: absolute; left: 1098px; top: 14px; width: 25px; }
  .menu span { display: block; height: 2px; background: #4a4a4a; margin-bottom: 3.5px; }
  .pitch {
    position: absolute; left: 689px; top: 250px; width: 440px; text-align: center; color: var(--teal);
  }
  .tagline { font-size: 16px; font-weight: 400; letter-spacing: 0.2px; }
  .brand { margin-top: 8px; font-size: 29px; font-weight: 300; color: var(--white); letter-spacing: 0.3px; }
  .headline { display: flex; align-items: center; justify-content: center; gap: 6px; }
  .headline h1 { font-size: 41px; font-weight: 400; letter-spacing: 0.5px; line-height: 1.1; }
  .rule { width: 63px; height: 8px; border-top: 2px solid var(--teal); border-bottom: 2px solid var(--teal); }
  .motto { font-size: 16px; font-weight: 400; margin-top: 8px; }
  .signup { position: absolute; left: 732px; top: 505px; width: 355px; text-align: center; }
  .signup p { color: var(--teal); font-size: 14px; margin-bottom: 9px; }
  .form { display: flex; height: 32px; border: 2px solid var(--teal-strong); border-radius: 4px; overflow: hidden; }
  .form .email { flex: 1; background: var(--field); color: var(--placeholder); font-size: 13px; text-align: left; padding: 6px 11px; }
  .form .notify { width: 85px; background: var(--teal-strong); color: var(--white); font-size: 14px; font-weight: 500; padding-top: 5px; }
</style>
</head>
<body>
  <main class="site">
    <div class="hero-photo" role="img" aria-label="Studio portrait of a young man in a white v-neck t-shirt and dark jeans against a grey wall"></div>

    <svg class="topbar" viewBox="0 0 1144 40" aria-hidden="true">
      <defs>
        <linearGradient id="barFill" x1="0" y1="0" x2="0" y2="1">
          <stop offset="0" stop-color="#0c0c0c"/>
          <stop offset="1" stop-color="#222222"/>
        </linearGradient>
      </defs>
      <path d="M0 0 H1085 L1072 32 Q1068 40 1056 40 H0 Z" fill="url(#barFill)"/>
    </svg>
    <nav class="social" aria-label="social links"><span></span><span></span><span></span><span></span></nav>
    <div class="menu" aria-label="menu"><span></span><span></span><span></span><span></span><span></span></div>

    <section class="pitch">
      <p class="tagline">it doesn't have to be complicated</p>
      <p class="brand">glowparlorqz</p>
      <div class="headline"><span class="rule"></span><h1>coming soon</h1><span class="rule"></span></div>
      <p class="motto">beauty, simplified.</p>
    </section>

    <section class="signup">
      <p>Get notified when our web site is live online</p>
      <div class="form">
        <div class="email">Enter your e-mail here</div>
        <div class="notify">Notify Me</div>
      </div>
    </section>
  </main>
</body>
</html>
```